New Creative Busines Card

Hi Lead Designer,

How are you going?

I was hoping you can help me design the perfect business card for my new business. I have listed below some background information about the business and the concept to help with your design. I'm open to any form of creative ideas, but would like to have two types of colour schemes one dark color and one light.

I would like to have a dark set of design and a light (One design with one in black or dark background and one with light background to compare the contrast since the business card will be double sided one) I imagine this will be pretty easy to change the background of the design. Would prefer one side to have all the details and the other will just have a amazing logo (K7) to give it the finishing touch.

Feel free to email me if you have any questions.

Business Structure and design concepts:

Name of the business: K7 Advisory
Business: Dating agency and event management (Date night etc)
Concept: The main focus will be the K7 ( As some sort of a heart shape like logo) be creative
Details to include in the card will be general details like Name, Title: , Email, mobile, website (Contact details will be given later).

The rest of the idea is up to you, feel free to go crazy with your creative ideas.

Thank you for your help in advance, may the best candidate win~!

Target Market(s)

Target market will be Professional, Elegant, young and ambitious people.

Industry/Entity Type

Business

Requirements
Must have
• Focus on the K7 (as some sort of a heart shape logo). Since this is a double sides design would prefer on one side to focus on the just the K7 logo and the other side with a smaller version of the logo (with it or without) and all the details such as Name, Title, Mobile, Email, Website. Please have the design in landscape format.Not fuss with the Font as long as it is easy to read.
Nice to have
• Different Contrast in colours (keep it simple) one side dark colour scheme and one side light. Prefer to have 3-4 colours (not overwhelm with too many colours) to keep it simple and elegant.
Should not have
• Too colours, main focus is should be the K7 logo not the colours

```html
<!DOCTYPE html>
<html lang="en">
<head>
<meta charset="utf-8">
<title>K7 Advisory – Business Card</title>
<link rel="stylesheet" href="https://fonts.googleapis.com/css2?family=Fira+Sans:wght@400;500&family=Open+Sans:wght@400&display=swap">
<style>
  :root {
    --page: #e3e3e3;
    --red: #e2232a;
    --red-deep: #c9161c;
    --white: #ffffff;
    --paper: #f7f7f7;
    --ink: #2e2e2e;
    --shadow: rgba(0, 0, 0, 0.22);
  }
  * { box-sizing: border-box; margin: 0; padding: 0; }
  html, body {
    width: 1169px;
    height: 1200px;
    overflow: hidden;
    background: var(--page);
  }
  .canvas {
    position: relative;
    width: 1169px;
    height: 1200px;
  }
  .card {
    position: absolute;
    left: 104px;
    width: 960px;
    height: 548px;
    border-radius: 34px;
    overflow: hidden;
    box-shadow: 0 14px 30px var(--shadow);
  }

  /* Front: dark side */
  .card--front { top: 40px; }
  .front-backdrop {
    position: absolute;
    inset: 0;
    background: radial-gradient(ellipse at 30% 20%, #ea3a40 0%, var(--red) 45%, var(--red-deep) 100%);
  }
  .front-content {
    position: absolute;
    inset: 0;
    display: flex;
    flex-direction: column;
    align-items: center;
    justify-content: center;
    gap: 34px;
    color: var(--white);
  }
  .rule {
    width: 560px;
    height: 2px;
    background: var(--white);
    opacity: 0.9;
  }
  .brand {
    display: flex;
    align-items: center;
    gap: 18px;
    font-family: "Fira Sans", sans-serif;
    font-weight: 500;
    font-size: 64px;
    letter-spacing: 1px;
  }
  .brand-dot {
    width: 26px;
    height: 26px;
    border-radius: 50%;
    background: currentColor;
  }
  .tagline {
    font-family: "Open Sans", sans-serif;
    font-size: 30px;
    letter-spacing: 1.5px;
  }

  /* Back: light side */
  .card--back {
    top: 620px;
    background: var(--paper);
  }
  .back-band {
    position: absolute;
    left: 0; right: 0; bottom: 0;
    height: 86px;
    background: var(--red);
  }
  .back-rule {
    position: absolute;
    left: 70px; right: 70px;
    height: 2px;
    background: var(--red);
  }
  .back-rule--top { top: 40px; }
  .back-rule--bottom { bottom: 116px; }
  .back-brand {
    position: absolute;
    top: 78px;
    left: 0; right: 0;
    display: flex;
    justify-content: center;
    align-items: center;
    gap: 14px;
    font-family: "Fira Sans", sans-serif;
    font-weight: 500;
    font-size: 46px;
    color: var(--ink);
  }
  .back-brand .brand-dot { width: 20px; height: 20px; background: var(--red); }
  .holder-name {
    position: absolute;
    top: 170px;
    left: 0; right: 0;
    text-align: center;
    font-family: "Fira Sans", sans-serif;
    font-size: 40px;
    color: var(--red);
  }
  .contact-list {
    position: absolute;
    top: 250px;
    left: 100px;
    right: 100px;
    display: flex;
    flex-wrap: wrap;
    justify-content: center;
    column-gap: 34px;
    row-gap: 16px;
    list-style: none;
    font-family: "Fira Sans", sans-serif;
    font-size: 25px;
    color: var(--ink);
  }
  .contact-item {
    display: flex;
    align-items: center;
    gap: 9px;
  }
  .contact-item svg {
    width: 24px;
    height: 24px;
    flex: none;
    fill: none;
    stroke: var(--red);
    stroke-width: 2;
  }
  .contact-item--address { flex-basis: 100%; justify-content: center; }
</style>
</head>
<body>
<main class="canvas">

  <section class="card card--front" aria-label="Card front">
    <div class="front-backdrop" role="img" aria-label="Red card background with a faint scattered heart pattern"></div>
    <div class="front-content">
      <div class="rule"></div>
      <div class="brand"><span class="brand-dot"></span>K7 Advisory</div>
      <p class="tagline">Dating agency and event management</p>
      <div class="rule"></div>
    </div>
  </section>

  <section class="card card--back" aria-label="Card back">
    <div class="back-rule back-rule--top"></div>
    <div class="back-brand"><span class="brand-dot"></span>K7 Advisory</div>
    <h1 class="holder-name">Maris Okonell</h1>
    <ul class="contact-list">
      <li class="contact-item">
        <svg viewBox="0 0 24 24"><path d="M5 3h4l2 5-2.5 1.5a11 11 0 0 0 6 6L16 13l5 2v4a2 2 0 0 1-2 2A16 16 0 0 1 3 5a2 2 0 0 1 2-2z"/></svg>
        555-014-2290
      </li>
      <li class="contact-item">
        <svg viewBox="0 0 24 24"><circle cx="12" cy="12" r="9"/><path d="M3 12h18M12 3c3 3 3 15 0 18M12 3c-3 3-3 15 0 18"/></svg>
        www.k7advisory-site.com
      </li>
      <li class="contact-item">
        <svg viewBox="0 0 24 24"><rect x="3" y="5" width="18" height="14"/><path d="M3 5l9 8 9-8"/></svg>
        hello@k7advisory-site.com
      </li>
      <li class="contact-item contact-item--address">
        <svg viewBox="0 0 24 24"><path d="M12 22s7-7 7-12a7 7 0 0 0-14 0c0 5 7 12 7 12z"/><circle cx="12" cy="10" r="2.5"/></svg>
        18/40, Linden Lane, North Park Avenue, USA
      </li>
    </ul>
    <div class="back-rule back-rule--bottom"></div>
    <div class="back-band"></div>
  </section>

</main>
</body>
</html>
```